Marvane seminar club leaflet

We need a flyer design to send out to various dog clubs and societies to promote a seminar on the law relating to dogs which we provide. These talks are both informative and entertaining and the main audience is middle aged responsible dog owners who are prepared to pay £20 to be given important information about how dog owners and others are affected by the many laws relating to dogs.

Details of how we operate these talks is important to convey to the clubs in terms of cost and numbers required etc. but we want them to appreciate that the talk itself does not cost the club and that we provide a proportion of the monies paid by the attendees to the club to cover their overheads anmd they often make a modest profit for the club.

We have uploaded 2 pdf's. One is the existing flyer which we want revamped and the other is a flyer which Halden Fold currently use which has a less stiff and formal feel to it which is what we're looking for.

A lot of the information on the leaflet is important and must be kept in but it may be that some of it might be unnecessary.

We're happy for a change of style to a lighter one and aren't married to any of the pictures either. The person with the dogs in the photos is Gilbert but perhaps we should not have any photographs at all - we're not sure. We're happy for alternative stock photos to be used of dogs or similar and don't necessarily want to stay with the red, grey and black on white background if we like the overall feel of the flyer.

```html
<!DOCTYPE html>
<html lang="en">
<head>
<meta charset="utf-8">
<title>Marvane seminar club leaflet</title>
<link rel="stylesheet" href="https://fonts.googleapis.com/css2?family=Montserrat:wght@400;500;700&family=Fredoka:wght@600&family=Poppins:wght@400;600&display=swap">
<style>
  :root {
    --ink: #1e2226;
    --slate: #2e3438;
    --slate-deep: #23282c;
    --paper: #ffffff;
    --stage: #ecebe8;
    --accent: #f7d21a;
    --sky-top: #6fa8dc;
    --sky-low: #b9d4ec;
    --coat: #c49468;
    --grass: #7fb24a;
    --rule: #8a8f93;
  }
  * { box-sizing: border-box; margin: 0; padding: 0; }
  html, body { width: 1200px; height: 795px; overflow: hidden; background: var(--stage); }
  body { font-family: "Montserrat", Arial, sans-serif; color: var(--ink); }

  .spread { position: relative; width: 1200px; height: 795px; display: flex; }
  .page { position: relative; width: 600px; height: 795px; background: var(--paper); overflow: hidden; }

  /* back page */
  .contact-band { position: absolute; left: 0; top: 0; width: 600px; height: 250px; background: var(--slate); padding: 34px 40px; color: var(--paper); }
  .contact-row { display: flex; align-items: center; gap: 18px; font-size: 27px; font-weight: 500; letter-spacing: 0.5px; margin-bottom: 14px; }
  .contact-icon { width: 40px; height: 40px; border: 2px solid var(--paper); border-radius: 50%; display: flex; align-items: center; justify-content: center; flex: none; }
  .partner-mark { margin: 18px 0 0 58px; display: flex; align-items: center; gap: 12px; }
  .partner-square { width: 26px; height: 26px; background: var(--accent); }
  .partner-name { font-size: 30px; font-weight: 700; color: var(--paper); }
  .partner-reg { margin: 8px 0 0 58px; font-size: 11px; color: #d6d9db; }

  .how-it-works { position: absolute; left: 40px; top: 282px; width: 530px; }
  .section-title { font-size: 20px; font-weight: 700; margin: 0 0 6px; }
  .steps { list-style: none; font-size: 16px; line-height: 1.3; margin-bottom: 14px; }
  .steps li { position: relative; padding-left: 32px; margin-bottom: 3px; }
  .steps li::before { content: ""; position: absolute; left: 2px; top: 5px; border-left: 12px solid var(--ink); border-top: 5px solid transparent; border-bottom: 5px solid transparent; }

  .enquiry { position: absolute; left: 40px; top: 600px; width: 530px; }
  .enquiry-note { font-size: 12.5px; line-height: 1.35; margin-bottom: 10px; }
  .field { display: flex; align-items: flex-end; gap: 8px; font-size: 14px; font-weight: 700; margin-bottom: 8px; }
  .field-line { flex: 1; border-bottom: 1px solid var(--rule); height: 14px; }

  /* cover */
  .hero-photo { position: absolute; left: 0; top: 0; width: 600px; height: 360px;
    background: linear-gradient(180deg, var(--sky-top) 0%, var(--sky-low) 30%, var(--coat) 55%, var(--coat) 82%, var(--grass) 100%); }
  .title-banner { position: absolute; left: 0; top: 340px; width: 430px; height: 180px; background: var(--slate-deep); display: flex; align-items: center; padding-left: 36px; }
  .title-banner h1 { font-family: "Fredoka", "Arial Rounded MT Bold", sans-serif; font-weight: 600; font-size: 72px; color: var(--paper); letter-spacing: 1px; }
  .tagline-box { position: absolute; left: 440px; top: 355px; width: 160px; height: 215px; background: var(--slate); color: var(--paper); text-align: center; padding: 14px 10px; }
  .badges { display: flex; justify-content: center; gap: 10px; margin-bottom: 12px; }
  .badge { width: 62px; height: 26px; background: var(--paper); border-radius: 3px; }
  .badge-round { width: 36px; border-radius: 50%; background: #e8efe0; }
  .tagline { font-family: "Poppins", Arial, sans-serif; font-weight: 600; font-size: 14px; line-height: 1.2; margin-bottom: 14px; }
  .presenter { font-size: 12.5px; line-height: 1.25; color: #d0d4d7; }
  .host-question { position: absolute; left: 40px; top: 588px; width: 540px; text-align: center; font-family: "Poppins", Arial, sans-serif; font-weight: 600; font-size: 34px; line-height: 1.15; }
  .host-note { position: absolute; left: 80px; top: 690px; width: 460px; text-align: center; font-family: "Poppins", Arial, sans-serif; font-size: 17px; line-height: 1.3; }
  .footer-stripe { position: absolute; left: 0; bottom: 0; width: 600px; height: 24px; background: var(--slate-deep); }
  .fold { position: absolute; left: 600px; top: 0; width: 1px; height: 795px; background: #d9dadb; }
</style>
</head>
<body>
<main class="spread">
  <section class="page back-page">
    <header class="contact-band">
      <div class="contact-row">
        <span class="contact-icon"><svg width="22" height="18" viewBox="0 0 22 18"><path d="M2 6c0-3 4-4 9-4s9 1 9 4l-3 1-1-2H6L5 7z" fill="#fff"/><rect x="5" y="9" width="12" height="7" rx="1.5" fill="#fff"/></svg></span>
        <span>020 7946 0318</span>
      </div>
      <div class="contact-row">
        <span class="contact-icon"><svg width="20" height="14" viewBox="0 0 20 14"><rect x="1" y="1" width="18" height="12" fill="none" stroke="#fff" stroke-width="1.8"/><path d="M1 1l9 7 9-7" fill="none" stroke="#fff" stroke-width="1.8"/></svg></span>
        <span>clubs@haldenfold.org.uk</span>
      </div>
      <div class="partner-mark">
        <span class="partner-square"></span>
        <span class="partner-name">Halden Fold</span>
      </div>
      <p class="partner-reg">Reg. Charity Numbers: 804117 &amp; SC052916</p>
    </header>

    <div class="how-it-works">
      <h2 class="section-title">The way it works, is that you:–</h2>
      <ul class="steps">
        <li>Provide the venue</li>
        <li>Obtain a minimum of 20 attendees</li>
        <li>Provide tea/coffee for when people arrive and at a break halfway through</li>
        <li>Promote the seminar to your members and locally to others</li>
      </ul>
      <h2 class="section-title">We will:–</h2>
      <ul class="steps">
        <li>Charge attendees £20 and pay you £5 for each paid attendee</li>
        <li>Provide you with colour information leaflets/booking forms for you to distribute</li>
        <li>Provide you with a pdf of the information leaflet/booking form for you to promote the event by email</li>
      </ul>
    </div>

    <form class="enquiry">
      <p class="enquiry-note">If you may be interested, or for further information, please complete the form below and post it to us at Marvane Limited, 14 Mill Lane, Ashworth, Kent CT9 4QR, Email us at talks@marvane.co.uk or telephone us on 01632 960452</p>
      <div class="field"><span>Your name :</span><span class="field-line"></span></div>
      <div class="field"><span>Your club's name :</span><span class="field-line"></span></div>
      <div class="field"><span>Telephone :</span><span class="field-line"></span></div>
      <div class="field"><span>Email :</span><span class="field-line"></span></div>
      <div class="field"><span>Any particular dates in mind for the seminar?:</span><span class="field-line"></span></div>
    </form>
  </section>

  <span class="fold"></span>

  <section class="page cover-page">
    <div class="hero-photo" role="img" aria-label="Photograph of a smiling bulldog against blue sky and grass"></div>
    <div class="title-banner"><h1>Marvane:</h1></div>
    <aside class="tagline-box">
      <div class="badges"><span class="badge"></span><span class="badge badge-round"></span></div>
      <p class="tagline">What every responsible dogowner needs to know.</p>
      <p class="presenter">Presented by 'The Hound Counsel'™ Gilbert Ashby, Solicitor</p>
    </aside>
    <h2 class="host-question">Would you like to host this seminar?</h2>
    <p class="host-note">It can be organised for any time over a weekend or a weekday evening.</p>
    <div class="footer-stripe"></div>
  </section>
</main>
</body>
</html>
```